Letterhead design for Dental Practice - Ashby Lane Dental Care

Letterhead for Private Dental Practice. To be used for all official correspondance and for printing treatment details on to be given to patients.

Target Market(s)

Private dental patients

Industry/Entity Type

Dental Clinic

Font styles to use
Other font styles liked:
• nexa-light

Colors
33a6d7
1c66ac
85abd2

Requirements
Must have
• info in the footer and header needs to be 3.5cm from upper/lower boader of paper, see photo in uploaded files
• info details:
• tel. 01632 960 305
• email info@ashbylanedc.co.uk
• ashbylanedentalcare.co.uk
• 17b Ashby Lane Fernleigh Kelmsworth KW4 7QT
• nexa-light font as in uploaded logo files
Should not have
• No funny tooth pictures

```html
<!DOCTYPE html>
<html lang="en">
<head>
<meta charset="utf-8">
<title>Ashby Lane Dental Care – Stationery</title>
<link href="https://fonts.googleapis.com/css2?family=Questrial&display=swap" rel="stylesheet">
<style>
  :root {
    --brand-blue: #1a9fdb;
    --ink: #3a3a3a;
    --rule: #3d3d3d;
    --paper: #ffffff;
    --cover: #f1f1f1;
    --backdrop: #e6e6e6;
  }
  * { margin: 0; padding: 0; box-sizing: border-box; }
  html, body { width: 1200px; height: 894px; overflow: hidden; }
  body {
    background: var(--backdrop);
    font-family: "Questrial", "Century Gothic", sans-serif;
    color: var(--ink);
    position: relative;
  }

  /* Letterhead sheet */
  .letterhead {
    position: absolute;
    left: 74px; top: 73px;
    width: 522px; height: 675px;
    background: var(--paper);
  }
  .letterhead__brand {
    position: absolute;
    left: 46px; top: 54px;
    display: flex; align-items: center; gap: 7px;
    color: var(--brand-blue);
    font-size: 15px;
    letter-spacing: 0.2px;
  }
  .brand-dot {
    width: 12px; height: 12px; border-radius: 50%;
    background: var(--brand-blue);
  }
  .letterhead__rule {
    position: absolute;
    left: 46px; top: 92px;
    width: 431px; height: 1px;
    background: var(--rule);
  }
  .letterhead__body {
    position: absolute;
    left: 55px; top: 117px;
    width: 411px;
    font-size: 11.2px;
    line-height: 17.1px;
    text-align: justify;
    hyphens: auto;
  }
  .letterhead__body p + p { margin-top: 17px; }

  .signature {
    position: absolute;
    left: 380px; top: 543px;
  }
  .signature__name { font-size: 14px; color: #333; }
  .signature__role { font-size: 9.6px; margin-top: 8px; }

  .contact {
    position: absolute;
    left: 47px; top: 602px;
    font-size: 7px;
    color: #555;
  }
  .contact__row { display: flex; align-items: center; gap: 5px; height: 12px; }
  .contact__row svg { width: 8px; height: 8px; }
  .contact__address {
    margin-top: 2px;
    color: var(--brand-blue);
    font-weight: bold;
    font-size: 6.8px;
  }

  .letterhead__footer {
    position: absolute;
    left: 0; bottom: 0;
    width: 100%; height: 25px;
    background: var(--brand-blue);
    color: #fff;
    display: flex; align-items: center; justify-content: center;
    font-size: 8.4px;
    font-weight: bold;
    letter-spacing: 2.2px;
    padding-right: 30px;
  }

  /* Folder cover */
  .folder {
    position: absolute;
    left: 638px; top: 72px;
    width: 498px; height: 675px;
    background: var(--cover);
    border-radius: 14px;
  }
  .folder__brand {
    position: absolute;
    left: 0; right: 0; top: 540px;
    display: flex; flex-direction: column; align-items: center;
    color: var(--brand-blue);
    font-size: 36px;
    line-height: 1.1;
    letter-spacing: 0.5px;
    padding-left: 20px;
  }
  .folder__brand span:last-child {
    font-size: 19px;
    letter-spacing: 7px;
    margin-top: 4px;
  }
</style>
</head>
<body>

<section class="letterhead">
  <div class="letterhead__brand">
    <span class="brand-dot"></span>
    <span>Ashby Lane Dental Care</span>
  </div>
  <div class="letterhead__rule"></div>

  <div class="letterhead__body">
    <p>Lorem ipsum dolor sit amet, consectetur adipiscing elit. Donec orci purus, luctus vitae dignissim eu, iaculis sed purus. Vivamus faucibus, ipsum nec aliquet viverra, leo mauris condimentum ligula, sit amet sagittis enim ligula quis arcu. Nam egestas tortor id nisi porttitor mattis. In tortor ante, ultricies in suscipit a, tempus non massa. Vivamus et auctor mi. Fusce vel massa nulla. Phasellus nec eros mauris, et scelerisque orci. Donec malesuada orci vitae nulla accumsan porta a id massa.</p>
    <p>Quisque accumsan iaculis magna sit amet fringilla. Maecenas consequat, magna eget tincidunt semper, odio nibh rutrum mi, id feugiat ante nisi eu risus. Vestibulum nunc orci, rhoncus a placerat in, ultricies in mi. Cras mattis varius eros, vel fringilla nisi suscipit eget. Quisque scelerisque sagittis nulla at porttitor. Mauris a justo et tellus interdum tristique. Sed id augue vitae urna euismod commodo aliquet a quam. Pellentesque arcu velit, cursus et malesuada ut, consequat et diam. Nullam erat sem, rhoncus id ullamcorper vitae, rhoncus et arcu. In ultricies ultricies nulla,</p>
    <p>Kut rutrum nisi iaculis at. Donec eu magna a metus ornare faucibus. Fusce aliquet faucibus ultricies. Morbi semper, est id tincidunt gravida, sem arcu adipiscing lacus, ac bibendum nulla leo eu purus. Quisque nec diam sed risus consectetur a ccumsan quis quis nibh. Vestibulum id purus lorem. Donec eu magna a metus ornare faucibus. Fusce aliquet faucibus ultricies. Morbi semper, est id tincidunt gravida, sem arcu adipiscing lacus, ac bibendum nulla leo eu purus. Quisque nec diam sed risus consectetur a ccumsan quis quis nibh. Vestibulum id purus lorem.</p>
  </div>

  <div class="signature">
    <div class="signature__name">Daniel Marsh</div>
    <div class="signature__role">Co-Founder &amp; CEO</div>
  </div>

  <div class="contact">
    <div class="contact__row">
      <svg viewBox="0 0 10 10" aria-hidden="true"><circle cx="5" cy="5" r="5" fill="#1a9fdb"/><path d="M3 3.2h4v1H3zM3.5 4.4h3l.6 2.4H2.9z" fill="#fff"/></svg>
      <span>01632 960 305</span>
    </div>
    <div class="contact__row">
      <svg viewBox="0 0 10 10" aria-hidden="true"><circle cx="5" cy="5" r="5" fill="#1a9fdb"/><rect x="2.5" y="3.3" width="5" height="3.4" fill="#fff"/><path d="M2.5 3.3L5 5.2 7.5 3.3" stroke="#1a9fdb" stroke-width=".6" fill="none"/></svg>
      <span>info@ashbylanedc.co.uk</span>
    </div>
    <div class="contact__address">17b Ashby Lane Fernleigh Kelmsworth KW4 7QT</div>
  </div>

  <footer class="letterhead__footer">www.ashbylanedentalcare.co.uk</footer>
</section>

<section class="folder">
  <div class="folder__brand">
    <span>Ashby Lane</span>
    <span>Dental Care</span>
  </div>
</section>

</body>
</html>
```